Women's Online Clothing Boutique Needs Business Cards

I already have a logo that I would like to use. Some of the things that interest me is black business cards, foil embossed logo, glossy embossed logo, leopard print, no yellow font, rounded edges. I even like just a large logo on the front side with all of my information on the back side.

Contact Information for Business Card

https://silverheron.shopvenlo.com/
https://www.pagelink.net/thesilverheronboutique/
https://www.picfeed.net/thesilverheronboutique/
silverheronboutique@mailora.net

Requirements
Must have
• My Logo
Nice to have
• Leopard Print
Should not have
• No Yellow Font

```html
<!DOCTYPE html>
<html lang="en">
<head>
<meta charset="utf-8">
<title>The Silver Heron Boutique – Business Cards</title>
<link rel="stylesheet" href="https://fonts.googleapis.com/css2?family=Josefin+Sans:wght@400&display=swap">
<style>
  :root {
    --backdrop: #3a3a3a;
    --card-white: #ffffff;
    --card-black: #121212;
    --ink: #1c1c1c;
    --logo-grey: #a8a8a8;
    --print-dark: #2a2a2a;
    --print-mid: #5a5a5a;
  }
  * { box-sizing: border-box; margin: 0; padding: 0; }
  html, body {
    width: 1200px; height: 900px; overflow: hidden;
    background: var(--backdrop);
    font-family: "Josefin Sans", Arial, sans-serif;
  }
  .sheet {
    position: relative; width: 1200px; height: 900px;
    display: flex; align-items: center; justify-content: center; gap: 60px;
  }
  .card {
    position: relative; width: 500px; height: 290px;
    border-radius: 22px; overflow: hidden;
  }
  .card--back { background: var(--card-white); }
  .card--front { background: var(--card-black); }

  .contact-list {
    position: absolute; top: 34px; left: 34px;
    list-style: none; display: flex; flex-direction: column; gap: 9px;
    color: var(--ink); font-size: 15px; letter-spacing: 0.2px;
  }
  .contact-list li { display: flex; align-items: center; gap: 10px; }
  .contact-icon { width: 14px; height: 14px; flex: none; }

  .print-area { position: absolute; inset: 0; width: 100%; height: 100%; }

  .front-texture { position: absolute; inset: 0; width: 100%; height: 100%; }
  .brand {
    position: absolute; inset: 0;
    display: flex; align-items: center; justify-content: center; gap: 18px;
  }
  .brand-mark {
    width: 58px; height: 58px; border-radius: 50%;
    background: var(--logo-grey); flex: none;
  }
  .brand-name {
    display: flex; flex-direction: column; align-items: center;
    color: var(--logo-grey); font-weight: 400; line-height: 1.1;
  }
  .brand-name__main { font-size: 40px; }
  .brand-name__sub { font-size: 30px; }
</style>
</head>
<body>
<main class="sheet">
  <section class="card card--back" aria-label="Business card back">
    <svg class="print-area" viewBox="0 0 500 290" role="img" aria-label="Black leopard print pattern covering the lower right of the card">
      <defs>
        <linearGradient id="printTone" x1="0" y1="0" x2="1" y2="1">
          <stop offset="0" stop-color="var(--print-mid)"/>
          <stop offset="1" stop-color="var(--print-dark)"/>
        </linearGradient>
      </defs>
      <path d="M500 40 L330 120 L290 160 L170 200 L90 230 L70 290 L500 290 Z" fill="url(#printTone)"/>
    </svg>
    <ul class="contact-list">
      <li>
        <svg class="contact-icon" viewBox="0 0 14 14" aria-hidden="true"><circle cx="7" cy="7" r="6" fill="none" stroke="var(--ink)" stroke-width="1.4"/><path d="M1 7h12M7 1c-3 3-3 9 0 12M7 1c3 3 3 9 0 12" fill="none" stroke="var(--ink)" stroke-width="1"/></svg>
        <span>silverheron.shopvenlo.com</span>
      </li>
      <li>
        <svg class="contact-icon" viewBox="0 0 14 14" aria-hidden="true"><circle cx="7" cy="7" r="6.5" fill="var(--ink)"/></svg>
        <span>/thesilverheronboutique</span>
      </li>
      <li>
        <svg class="contact-icon" viewBox="0 0 14 14" aria-hidden="true"><circle cx="7" cy="7" r="6.5" fill="var(--ink)"/></svg>
        <span>/thesilverheronboutique</span>
      </li>
      <li>
        <svg class="contact-icon" viewBox="0 0 14 14" aria-hidden="true"><rect x="1" y="3" width="12" height="8" fill="none" stroke="var(--ink)" stroke-width="1.4"/><path d="M1 3l6 5 6-5" fill="none" stroke="var(--ink)" stroke-width="1.2"/></svg>
        <span>silverheronboutique@mailora.net</span>
      </li>
    </ul>
  </section>

  <section class="card card--front" aria-label="Business card front">
    <svg class="front-texture" viewBox="0 0 500 290" role="img" aria-label="Faint tone-on-tone leopard print texture">
      <defs>
        <radialGradient id="frontTone" cx="0.5" cy="0.5" r="0.7">
          <stop offset="0" stop-color="#222222"/>
          <stop offset="1" stop-color="var(--card-black)"/>
        </radialGradient>
      </defs>
      <rect width="500" height="290" fill="url(#frontTone)"/>
    </svg>
    <div class="brand">
      <h1 class="brand-name">
        <span class="brand-name__main">The Silver Heron</span>
        <span class="brand-name__sub">Boutique</span>
      </h1>
      <span class="brand-mark" aria-hidden="true"></span>
    </div>
  </section>
</main>
</body>
</html>
```